Online Travel Agency card design with 2 logos

Need a two sided business card design for online tourism agency which is based in Istanbul Turkey.
Need a business card design where it shows the travel agency logo but also the logo and information of the parent company as well.Parent company logo is just text with 2 different colors. (Arial font with text TemaVista "Tema"- hex #172841 and "Vista" hex-#FF7F00)
Both logos are uploaded.
Target Market(s)
travel , online
Industry/Entity Type
Travel
Contact Information for Business Card
The information on the card should be as :
Travel Agency Logo logo (rnlogo)
Parent Company logo(temalogo)
Company information :TemaVista Turizm ve Bilgi Teknolojileri A.Ş
Address of company
Tel
Email
Name
Position(english and turkish)
Look and feel
Each slider illustrates characteristics of the customer's brand and the style your logo design should communicate.

```html
<!DOCTYPE html>
<html lang="en">
<head>
<meta charset="utf-8">
<title>rotanet — Business Card</title>
<link href="https://fonts.googleapis.com/css2?family=Lato:wght@400;700;900&display=swap" rel="stylesheet">
<style>
  :root {
    --backdrop: #2e1c13;
    --navy: #152842;
    --sky: #6ccbe6;
    --ink: #1b1f2a;
    --paper: #ffffff;
    --divider: #2a2f38;
  }
  * { margin: 0; padding: 0; box-sizing: border-box; }
  html, body { width: 1200px; height: 1000px; overflow: hidden; }
  body {
    background: var(--backdrop);
    font-family: 'Lato', Arial, sans-serif;
    position: relative;
  }
  .card {
    position: absolute;
    width: 517px;
    height: 293px;
    border-radius: 16px;
    overflow: hidden;
    box-shadow: 0 4px 8px rgba(0,0,0,0.35);
  }
  .card--front { left: 349px; top: 212px; background: var(--paper); }
  .card--back  { left: 351px; top: 536px; background: var(--navy); }

  .front__brand {
    position: absolute;
    right: 272px;
    top: 76px;
    text-align: right;
  }
  .agency-mark {
    display: flex;
    align-items: center;
    justify-content: flex-end;
    gap: 6px;
  }
  .agency-mark__dot {
    width: 28px; height: 28px; border-radius: 50%;
    background: var(--navy);
  }
  .agency-mark__name {
    font-size: 26px; font-weight: 700; color: var(--navy);
    letter-spacing: -0.5px; line-height: 1;
  }
  .parent-mark {
    margin-top: 6px;
    font-size: 20px; font-weight: 700; color: var(--navy);
    line-height: 1;
  }
  .company-legal {
    margin-top: 12px;
    font-size: 14.5px; color: var(--ink); line-height: 1.2;
  }
  .front__divider {
    position: absolute;
    left: 280px; top: 57px;
    width: 1.5px; height: 148px;
    background: var(--divider);
  }
  .front__contact {
    position: absolute;
    left: 315px; top: 57px;
    color: var(--ink);
  }
  .person__name {
    font-size: 21px; font-weight: 900; color: var(--ink);
    letter-spacing: 0.5px; line-height: 1.1;
  }
  .person__name span { color: var(--sky); }
  .person__role { font-size: 15.5px; margin-top: 2px; }
  .contact-list { margin-top: 14px; font-size: 13.8px; line-height: 17px; }
  .contact-list__address { margin-top: 5px; }
  .front__band { position: absolute; left: 0; bottom: 0; }

  .back__circle-shadow {
    position: absolute; left: 40px; top: 48px;
    width: 194px; height: 194px; border-radius: 50%;
    background: #0a1424;
  }
  .back__circle {
    position: absolute; left: 36px; top: 46px;
    width: 194px; height: 194px; border-radius: 50%;
    background: var(--paper);
  }
  .back__name {
    position: absolute; left: 236px; top: 182px;
    font-size: 38px; font-weight: 700; color: var(--paper);
    letter-spacing: -0.5px; line-height: 1;
  }
</style>
</head>
<body>
  <section class="card card--front">
    <div class="front__brand">
      <div class="agency-mark">
        <span class="agency-mark__dot"></span>
        <span class="agency-mark__name">rotanet</span>
      </div>
      <div class="parent-mark">TemaVista</div>
      <p class="company-legal">TemaVista Turizm ve Bilgi<br>Teknolojileri A.Ş</p>
    </div>
    <div class="front__divider"></div>
    <div class="front__contact">
      <h1 class="person__name">JOHN <span>DOE</span></h1>
      <p class="person__role">Manager</p>
      <div class="contact-list">
        <p>01 123 456 7890</p>
        <p>youremail@domain.com</p>
        <p>www.yourwebsite.com</p>
        <p class="contact-list__address">41 Harbor Lane<br>Linden, VA 24099</p>
      </div>
    </div>
    <svg class="front__band" width="517" height="36" viewBox="0 0 517 36">
      <rect x="0" y="18" width="517" height="18" fill="var(--sky)"/>
      <path d="M216 36 L226 10 Q230 0 244 0 L517 0 L517 36 Z" fill="var(--navy)"/>
    </svg>
  </section>

  <section class="card card--back">
    <div class="back__circle-shadow"></div>
    <div class="back__circle"></div>
    <div class="back__name">rotanet</div>
  </section>
</body>
</html>
```